Oil Manufacturer Needs a Label Design

We need a label design for a new company based in North East Ohio called "BOLT up!" We process and manufacture Cutting Oil for consumers in the machining industry. Our product is a premium multi-purpose nonsoluble cutting oil. Machinists use this oil to keep their workpiece at a stable temperature, maximize tool life, and works to prevent rust on machine parts and cutters. The final design should relay the image of reliability and performance, and innovative to promote new sales. The labels will be for two different sized bottles: 4.25heightx5.5width and 2x4 inches. The label must include "Made in USA" and Net Wt 1 Gallon U.S. (3.75 Liters).

Please note: this oil is being purchased by customers who use tools to cut metal for a living. They are skilled machinists who need a reliable oil.

BACK LABEL: This label will be going on 1 gallon jugs (similar to windshield washer fluid containers) as well as 8oz smaller containers. The large 1 gallon jugs will need to have a back label that includes directions for use, cautions, our email and web address, and a space for a bar code.
Updates

Project Deadline Extended Reason: I am extending the deadline by 5 days because I have not received many designs and I had to make an update to my brief which involves the back label for the product. Please see project description in my brief. Added Wednesday, January 14, 2015

Target Market(s)

Machine shop laborers

Industry/Entity Type

Industry

Requirements
Must have
• BOLT up!
• Multi Purpose Non Soluble Cutting Oil
• Net 1 Gallon U.S.
• (3.785 Liters)
• CAUTION See Back Panel
• Made in U.S.A.
Nice to have
• Needs to look industrial and professional. Should look sleek and streamlined.
• Slogan: BOLT up! GRIND on! DRILL fast! STAY cool!
Should not have
• No crazy kid colors.

```html
<!DOCTYPE html>
<html lang="en">
<head>
<meta charset="utf-8">
<title>BOLT up! Cutting Oil Labels</title>
<link href="https://fonts.googleapis.com/css2?family=Oswald:wght@500;600;700&family=Archivo+Black&display=swap" rel="stylesheet">
<style>
  :root {
    --backdrop: #4a4541;
    --label-black: #111111;
    --label-grey: #2b2b2b;
    --orange: #f08a24;
    --orange-deep: #c0580f;
    --brown: #a9530f;
    --white: #ffffff;
    --ink: #111111;
    --band-grey: #333333;
    --steel-light: #e4e4e4;
    --steel-dark: #8d8d8d;
  }
  * { box-sizing: border-box; margin: 0; padding: 0; }
  html, body { width: 1200px; height: 900px; overflow: hidden; }
  body {
    position: relative;
    background: var(--backdrop);
    font-family: "Oswald", "Arial Narrow", sans-serif;
  }
  .label {
    position: absolute;
    overflow: hidden;
    border-radius: 8px;
    background: radial-gradient(circle at 45% 55%, var(--label-grey) 0%, var(--label-black) 70%);
    box-shadow: 0 2px 8px rgba(0,0,0,.45);
    color: var(--white);
  }
  .label--gallon { left: 513px; top: 80px; width: 550px; height: 718px; }
  .label--small  { left: 147px; top: 278px; width: 259px; height: 520px; }

  .product-type {
    position: absolute;
    font-weight: 600;
    line-height: 1.12;
    letter-spacing: .2px;
  }
  .label--gallon .product-type { left: 85px; top: 18px; font-size: 40px; }
  .label--small .product-type  { left: 21px; top: 22px; font-size: 19px; }

  .saw-blade {
    position: absolute;
    border-radius: 50%;
    background: radial-gradient(circle at 40% 35%, var(--steel-light), var(--steel-dark));
  }
  .label--gallon .saw-blade { left: 97px; top: 205px; width: 310px; height: 310px; }
  .label--small .saw-blade  { left: 43px; top: 130px; width: 160px; height: 160px; }

  .brand-name {
    position: absolute;
    color: var(--orange);
    font-weight: 700;
    line-height: .95;
    text-align: center;
  }
  .label--gallon .brand-name { left: 60px; top: 130px; width: 420px; font-size: 120px; }
  .label--small .brand-name  { left: 45px; top: 100px; width: 170px; font-size: 58px; }

  .slogan { position: absolute; list-style: none; }
  .slogan__band {
    position: absolute;
    right: -20px;
    transform: rotate(-5deg);
    transform-origin: right center;
    font-family: "Archivo Black", "Arial Black", sans-serif;
    display: flex;
    align-items: center;
    padding-left: 22px;
    white-space: nowrap;
  }
  .slogan__band--orange { background: var(--orange); color: var(--white); }
  .slogan__band--white  { background: var(--white); color: var(--ink); }
  .slogan__band--grey   { background: var(--band-grey); color: var(--white); }
  .slogan__band--brown  { background: var(--brown); color: var(--ink); }

  .label--gallon .slogan { left: 0; top: 0; width: 550px; height: 718px; }
  .label--gallon .slogan__band { height: 48px; font-size: 29px; }
  .label--gallon .slogan__band--orange { top: 420px; width: 270px; }
  .label--gallon .slogan__band--white  { top: 476px; width: 310px; }
  .label--gallon .slogan__band--grey   { top: 532px; width: 295px; }
  .label--gallon .slogan__band--brown  { top: 588px; width: 235px; }

  .label--small .slogan { left: 0; top: 0; width: 259px; height: 520px; }
  .label--small .slogan__band { height: 30px; font-size: 16px; padding-left: 16px; }
  .label--small .slogan__band--orange { top: 298px; width: 180px; }
  .label--small .slogan__band--white  { top: 330px; width: 210px; }
  .label--small .slogan__band--grey   { top: 364px; width: 185px; }
  .label--small .slogan__band--brown  { top: 398px; width: 160px; }

  .origin {
    position: absolute;
    font-family: "Archivo Black", "Arial Black", sans-serif;
    transform: rotate(-90deg);
    transform-origin: left top;
    white-space: nowrap;
  }
  .label--gallon .origin { left: 28px; top: 640px; font-size: 24px; }
  .label--small .origin  { left: 22px; top: 464px; font-size: 16px; }

  .caution { position: absolute; color: var(--orange); font-weight: 500; line-height: 1.05; }
  .label--gallon .caution { left: 67px; top: 604px; font-size: 14px; }
  .label--small .caution  { left: 121px; top: 455px; font-size: 10px; }

  .net-content {
    position: absolute;
    background: linear-gradient(var(--orange), var(--orange-deep));
    color: var(--ink);
    font-weight: 600;
    text-align: center;
  }
  .label--gallon .net-content { left: 9px; right: 11px; top: 668px; height: 46px; font-size: 27px; line-height: 46px; }
  .label--small .net-content  { left: 8px; right: 8px; top: 486px; height: 27px; font-size: 16px; line-height: 27px; }
</style>
</head>
<body>
  <article class="label label--small" aria-label="Small bottle front label">
    <h2 class="product-type">Multi Purpose<br>Non Soluble Cutting Oil</h2>
    <div class="saw-blade" role="img" aria-label="Steel saw blade illustration with an oil drop"></div>
    <p class="brand-name">BOLT up!</p>
    <ul class="slogan">
      <li class="slogan__band slogan__band--orange">BOLT up!</li>
      <li class="slogan__band slogan__band--white">GRIND on!</li>
      <li class="slogan__band slogan__band--grey">DRILL fast!</li>
      <li class="slogan__band slogan__band--brown">STAY cool!</li>
    </ul>
    <p class="origin">Made in U.S.A.</p>
    <p class="caution">CAUTION: See Back Panel</p>
    <p class="net-content">Net 1 Gallon U.S./ 3.785 Liters</p>
  </article>

  <article class="label label--gallon" aria-label="Gallon jug front label">
    <h1 class="product-type">Multi Purpose<br>Non Soluble Cutting Oil</h1>
    <div class="saw-blade" role="img" aria-label="Steel saw blade illustration with an oil drop"></div>
    <p class="brand-name">BOLT up!</p>
    <ul class="slogan">
      <li class="slogan__band slogan__band--orange">BOLT up!</li>
      <li class="slogan__band slogan__band--white">GRIND on!</li>
      <li class="slogan__band slogan__band--grey">DRILL fast!</li>
      <li class="slogan__band slogan__band--brown">STAY cool!</li>
    </ul>
    <p class="origin">Made in U.S.A.</p>
    <p class="caution">CAUTION:<br>See Back Panel</p>
    <p class="net-content">Net 1 Gallon U.S./ 3.785 Liters</p>
  </article>
</body>
</html>
```